Logo/ business card idea for a weld inspection/ nondestructive testing LLC

I have just started an LLC (my first) for weld inspection and non-destructive testing. I am the president and only member of this company. It is a very niche industry and word of mouth is basically the only advertisement needed to get you the next job. I will offer magnetic particle, dye penetrant, ultrasonic, and visual testing for the non-destructive services. X-ray is a form of non-destructive testing that I spent a few years doing but to costly for me at this time. All pipelines under the ground are welded, visually inspected and x-ray by someone just like me. All new building construction, any type of nuclear plant , pressure vessel, ect. , the welds are inspected by someone like me. Its is every increasing also with safety concerns. People are living right next to this stuff!!I will be the guy that fabrication shops or construction companies call to give the final OK that the welds are satisfactory after inspection to a certain code or standard. The designers have all the freedom they wish but I have attached a PDF with greater explanations and color ideas. I want raised glossy print on the front of the card and the necessary info. The back will not have raised print and serve more as a brief resume listing the certifications I have. The company only cares about the certifications and ultimately my signature. I want to make the front of the car into a fridge magnet to pass out with the card also. Something that is appealing to hang up instead of getting lost in someones wallet. The final design………. should be classic and stand the test of time. It should communicate precision and accuracy as well as incorporate the sound beam you will find in the PDF I’ve attached.Thanks and have a great day,Dale

Target Market(s)

Adult males in english speaking countries that handle welding and/or construction duties. Most of the time under heavy time constraints and deadlines. Ages 30-60

Industry/Entity Type

Construction

Contact Information for Business Card

Halvern Inspection Services, LLC
Dale Halvern
Ithaca, MI
989-514-2730
halv7dw@mailbreeze.net

Font styles to use
Other font styles liked:
• designers choice

Requirements
Nice to have
• The logo on the front can completely encase the Halvern, be segmented incorporating the Halvern, or next to it. There can also be a couple of “flaws” (the red, blue and yellow in some of the pictures attached in the PDF) in the sound beam spread.

```html
<!DOCTYPE html>
<html lang="en">
<head>
<meta charset="utf-8">
<title>Halvern Inspection Services, LLC — Business Card</title>
<link rel="stylesheet" href="https://fonts.googleapis.com/css2?family=Roboto:wght@400;700&display=swap">
<style>
  :root {
    --page: #ffffff;
    --charcoal: #2b2a29;
    --brand-red: #e30613;
    --ink: #1d1d1b;
    --ink-soft: #2f2f2f;
    --white: #ffffff;
    --silver-dark: #bcbcbc;
    --silver-mid: #d6d6d6;
    --silver-light: #f7f7f7;
    --beam-blue: #2aa6df;
    --beam-yellow: #ffed00;
    --beam-tan: #c9ab6a;
  }
  * { margin: 0; padding: 0; box-sizing: border-box; }
  html, body { width: 1014px; height: 1200px; overflow: hidden; background: var(--page); }
  body { position: relative; font-family: "Roboto", Arial, sans-serif; color: var(--ink); }

  .card {
    position: absolute; left: 75px; width: 845px; height: 480px; overflow: hidden;
    background: linear-gradient(90deg, var(--silver-dark) 0%, var(--silver-light) 45%, var(--silver-light) 60%, var(--silver-mid) 100%);
    box-shadow: 8px 10px 14px rgba(0,0,0,0.28);
  }
  .card--front { top: 64px; }
  .card--back { top: 634px; }

  .card__header { position: absolute; left: 0; top: 0; width: 100%; background: var(--charcoal); }
  .card--front .card__header { height: 193px; }
  .card--back .card__header { height: 170px; }

  .brand { position: absolute; line-height: 1; }
  .card--front .brand { left: 88px; top: 64px; }
  .card--back .brand { left: 181px; top: 54px; }
  .brand__name { display: block; font-weight: 700; font-size: 56px; color: var(--brand-red); letter-spacing: 1px; }
  .brand__tagline { display: block; margin-top: 6px; font-weight: 400; font-size: 23px; color: var(--white); padding-left: 16px; }

  .beam-band {
    position: absolute; left: 0; top: 193px; width: 100%; height: 144px;
    background: linear-gradient(90deg, #bdbdbd 0%, #d0d0d0 40%, #e9e9e9 80%, #f4f4f4 100%);
  }
  .beam-art { position: absolute; left: 0; top: 0; }

  .contact { position: absolute; top: 370px; left: 0; width: 100%; height: 70px; }
  .contact__person { position: absolute; right: 448px; top: 2px; text-align: right; }
  .contact__name { font-weight: 700; font-size: 27px; color: var(--ink); line-height: 1.2; }
  .contact__role { font-size: 20px; color: var(--ink-soft); line-height: 1.2; }
  .contact__divider { position: absolute; left: 426px; top: 0; width: 2px; height: 62px; background: var(--ink); }
  .contact__lines { position: absolute; left: 458px; top: 2px; list-style: none; }
  .contact__lines li { display: flex; align-items: center; gap: 10px; font-weight: 700; font-size: 21px; height: 34px; }
  .contact__icon { width: 22px; height: 22px; flex: none; }

  .credentials { position: absolute; left: 313px; top: 200px; list-style: none; font-size: 23px; color: var(--ink-soft); }
  .credentials li { position: relative; padding-left: 21px; height: 42px; line-height: 30px; }
  .credentials li.is-bullet::before {
    content: ""; position: absolute; left: 0; top: 12px; width: 7px; height: 7px; border-radius: 50%; background: var(--brand-red);
  }
  .credentials li.is-sub { padding-left: 123px; }
</style>
</head>
<body>

<section class="card card--front" aria-label="Business card front">
  <header class="card__header">
    <div class="brand">
      <span class="brand__name">HALVERN</span>
      <span class="brand__tagline">Inspection Services, LLC</span>
    </div>
  </header>

  <div class="beam-band">
    <svg class="beam-art" width="845" height="144" viewBox="0 0 845 144" role="img" aria-label="Crossing sound beam lines in red, blue and yellow">
      <defs>
        <linearGradient id="beam-tan" x1="0" y1="0" x2="1" y2="0">
          <stop offset="0" stop-color="var(--beam-tan)" stop-opacity="0.15"/>
          <stop offset="1" stop-color="var(--beam-tan)" stop-opacity="0.8"/>
        </linearGradient>
        <linearGradient id="beam-mix" x1="0" y1="0" x2="1" y2="0">
          <stop offset="0" stop-color="var(--brand-red)" stop-opacity="0.55"/>
          <stop offset="0.5" stop-color="var(--beam-blue)" stop-opacity="0.55"/>
          <stop offset="1" stop-color="var(--beam-yellow)" stop-opacity="0.65"/>
        </linearGradient>
      </defs>
      <polygon points="104,0 245,0 285,144 250,144" fill="url(#beam-tan)"/>
      <polygon points="245,0 690,0 570,144 285,144" fill="url(#beam-mix)"/>
    </svg>
  </div>

  <div class="contact">
    <div class="contact__person">
      <p class="contact__name">Dale Halvern</p>
      <p class="contact__role">IWC Certified Welding Inspector</p>
    </div>
    <span class="contact__divider"></span>
    <ul class="contact__lines">
      <li>
        <svg class="contact__icon" viewBox="0 0 24 24" aria-hidden="true">
          <path d="M6.6 2.5l3 4-2 2.2c1 2.4 3 4.6 5.6 6l2.1-2 4.2 2.8-1.5 3.6c-7.4.3-15-8.4-14-14.8z" fill="none" stroke="var(--brand-red)" stroke-width="2.2" stroke-linejoin="round"/>
        </svg>
        989-514-2730
      </li>
      <li>
        <svg class="contact__icon" viewBox="0 0 24 24" aria-hidden="true">
          <rect x="2" y="5" width="20" height="14" fill="none" stroke="var(--brand-red)" stroke-width="2"/>
          <path d="M2 5l10 8 10-8" fill="none" stroke="var(--brand-red)" stroke-width="2"/>
        </svg>
        halv7dw@mailbreeze.net
      </li>
    </ul>
  </div>
</section>

<section class="card card--back" aria-label="Business card back">
  <header class="card__header">
    <div class="brand">
      <span class="brand__name">HALVERN</span>
      <span class="brand__tagline">Inspection Services, LLC</span>
    </div>
  </header>

  <svg class="beam-art" width="400" height="480" viewBox="0 0 400 480" role="img" aria-label="Sweeping sound beam lines in red, blue and yellow">
    <defs>
      <linearGradient id="beam-sweep" x1="0" y1="0" x2="1" y2="1">
        <stop offset="0" stop-color="var(--brand-red)" stop-opacity="0.8"/>
        <stop offset="0.5" stop-color="var(--beam-blue)" stop-opacity="0.6"/>
        <stop offset="1" stop-color="var(--beam-yellow)" stop-opacity="0.75"/>
      </linearGradient>
    </defs>
    <polygon points="0,0 30,0 200,200 380,480 0,480" fill="url(#beam-sweep)"/>
  </svg>

  <ul class="credentials">
    <li class="is-bullet">IWC Certified Welding Inspector</li>
    <li class="is-bullet">IWC Certified Radiographic Interpreter</li>
    <li class="is-bullet">IWC Certified Welding Educator</li>
    <li class="is-bullet">Level II - Ultrasonic Testing</li>
    <li class="is-sub">Magnetic Particle Testing</li>
    <li class="is-sub">Liquid Penetrant Testing</li>
  </ul>
</section>

</body>
</html>
```